BRIGHT PEAK POWER.

I'd like my business logo.
contact name: Daniel Fitzhume
phone:0407395182
email: info@brightpeakpower.net.au
website: www.brightpeakpower.net.au

services:
solar
battery storage
LED lighting
energy saving solutions
general electrical
I'd like the design to look professional

Target Market(s)

Everyone

Industry/Entity Type

Business

Contact Information for Business Card

as described above

Requirements
Must have
• Id like the colours and the design to work well with my logo.

```html
<!DOCTYPE html>
<html lang="en">
<head>
<meta charset="utf-8">
<title>Bright Peak Power – Business Card</title>
<link href="https://fonts.googleapis.com/css2?family=Lato:wght@300;400;700;900&display=swap" rel="stylesheet">
<style>
  :root {
    --stage: #1c1c1c;
    --card-light: #f7f7f5;
    --card-dark: #121212;
    --ink: #3a3a3a;
    --green: #7cbf3a;
    --green-deep: #2f6b1f;
    --amber: #f0b323;
    --sun-tint: #f4e6c4;
  }
  * { box-sizing: border-box; margin: 0; padding: 0; }
  html, body { width: 1200px; height: 900px; overflow: hidden; }
  body {
    background: var(--stage);
    font-family: "Lato", sans-serif;
    display: flex; flex-direction: column; align-items: center; justify-content: center;
    gap: 40px;
  }
  .card {
    width: 700px; height: 400px; border-radius: 18px; position: relative; overflow: hidden;
  }
  /* Front */
  .card-front { background: var(--card-light); color: var(--ink); }
  .brand-mark-faint {
    position: absolute; left: 300px; top: 70px; width: 240px; height: 240px;
    border-radius: 50%; background: var(--sun-tint); opacity: .45;
  }
  .contact-row {
    position: absolute; display: flex; align-items: center; gap: 10px;
    font-size: 17px; font-weight: 300; letter-spacing: .3px;
  }
  .contact-icon {
    width: 22px; height: 22px; border-radius: 5px; background: var(--green);
    display: flex; align-items: center; justify-content: center;
  }
  .contact-phone { left: 40px; top: 44px; }
  .contact-email { left: 150px; top: 250px; }
  .contact-web { left: 420px; top: 300px; }
  .person { position: absolute; left: 190px; top: 120px; }
  .person-name {
    font-size: 46px; font-weight: 300; letter-spacing: 1px; text-transform: uppercase; line-height: 1;
  }
  .person-name .surname { color: var(--green); }
  .person-title {
    margin-top: 6px; font-size: 19px; font-weight: 300; letter-spacing: 3px; text-transform: uppercase;
  }
  .company { position: absolute; left: 40px; top: 300px; }
  .company-name {
    color: var(--green-deep); font-weight: 700; font-size: 18px; letter-spacing: .5px;
  }
  .company-address {
    margin-top: 4px; font-size: 16px; font-weight: 300; text-transform: uppercase; letter-spacing: .5px;
  }
  .rule-solid { position: absolute; left: 0; right: 0; bottom: 26px; height: 2px; background: var(--green-deep); }
  .rule-dotted { position: absolute; left: 0; right: 0; bottom: 18px; border-top: 2px dotted #9a9a9a; }
  /* Back */
  .card-back { background: linear-gradient(160deg, #1e1e1e, var(--card-dark)); }
  .brand {
    position: absolute; right: 60px; top: 110px; display: flex; align-items: center; gap: 18px;
  }
  .brand-dot { width: 56px; height: 56px; border-radius: 50%; background: var(--green); }
  .brand-name {
    color: var(--green); font-weight: 900; font-size: 44px; letter-spacing: 1px; line-height: 1;
  }
  .services {
    position: absolute; left: 40px; right: 40px; bottom: 90px;
    display: flex; gap: 22px; list-style: none; justify-content: center;
  }
  .service {
    color: var(--green); font-size: 19px; font-weight: 400; display: flex; align-items: center; gap: 6px;
  }
  .service::before {
    content: ""; width: 11px; height: 11px; background: var(--amber); display: block;
  }
</style>
</head>
<body>
  <section class="card card-front">
    <div class="brand-mark-faint"></div>

    <div class="contact-row contact-phone">
      <span class="contact-icon">
        <svg width="14" height="14" viewBox="0 0 24 24"><path fill="#fff" d="M6.6 10.8a15 15 0 0 0 6.6 6.6l2.2-2.2a1 1 0 0 1 1-.25 11.4 11.4 0 0 0 3.6.57 1 1 0 0 1 1 1V20a1 1 0 0 1-1 1A17 17 0 0 1 3 4a1 1 0 0 1 1-1h3.5a1 1 0 0 1 1 1c0 1.25.2 2.45.57 3.57a1 1 0 0 1-.25 1z"/></svg>
      </span>
      <span>0407 395 182</span>
    </div>

    <div class="person">
      <h1 class="person-name">Daniel <span class="surname">Fitzhume</span></h1>
      <p class="person-title">Managing Director</p>
    </div>

    <div class="contact-row contact-email">
      <span class="contact-icon">
        <svg width="14" height="14" viewBox="0 0 24 24"><circle cx="12" cy="12" r="4" fill="none" stroke="#fff" stroke-width="2.4"/><path d="M16 8v5a3 3 0 0 0 6 0v-1a10 10 0 1 0-4 8" fill="none" stroke="#fff" stroke-width="2.4"/></svg>
      </span>
      <span>info@brightpeakpower.net.au</span>
    </div>

    <div class="contact-row contact-web">
      <span class="contact-icon">
        <svg width="14" height="14" viewBox="0 0 24 24" fill="none" stroke="#fff" stroke-width="2"><circle cx="12" cy="12" r="9"/><path d="M3 12h18M12 3c3 3 3 15 0 18M12 3c-3 3-3 15 0 18"/></svg>
      </span>
      <span>www.brightpeakpower.net.au</span>
    </div>

    <div class="company">
      <p class="company-name">BRIGHT PEAK POWER SOLUTIONS</p>
      <p class="company-address">48 Harwood Lane, Alfredton VIC 3350</p>
    </div>

    <div class="rule-solid"></div>
    <div class="rule-dotted"></div>
  </section>

  <section class="card card-back">
    <div class="brand">
      <span class="brand-dot"></span>
      <span class="brand-name">BRIGHT PEAK POWER</span>
    </div>
    <ul class="services">
      <li class="service">LED Lighting</li>
      <li class="service">Battery Storage</li>
      <li class="service">Solar</li>
      <li class="service">Energy Saving Solutions</li>
    </ul>
  </section>
</body>
</html>
```